Scrum Master & Agile IT Coach Needing Business Website

Hello, my name is Brent Holloway
I am a project manger, scrum master, & agile coach. I work with IT development teams on major projects for Fortune 500 companies . My project management business has a website and can be found here: www.tq-keystride.example

I have launched a new company, ALL focused on IT Agile Coaching, I am looking to have a website created for my new company - the name of the new company is: Pins and Dials - Agile IT Coaching and Training.
I have a logo and it is provided in the materials. I like to logo; I am open to different color pallets.

The website will have a total of 7 pages; I have content for 5 of the 7 pages prepared; the other 2 pages will say under construction.

Page 1 Who am I, What I do, My Experience
Demonstrated experience and progression from Scrum Master to
Program Manager to Coach

Page 2 Pins & Dials - Agile Team Coaching
teams working major IT projects, multiple months/years

Page 3 Coaching @ the Team Level

Page 4 Coaching @ the Program Level ; LYNQ BQR level

Pages 5 -6 Under Construction

Page 7 Presentations, Slide Decks, Reference Materials

Mentor Nook need to have this highlighted somewhere Monthly Blog
Updates

Industry/Entity Type

IT development

Coding

Coded - Design and coding required

Number of Pages Required

5+ page

Requirements
Must have
• the website must be bold - I want those who visit to remember coming to my coaching site
Nice to have
• nice to have will be a modern / futuristic website; I work with IT developers, I want a website they will like
Should not have
• should not be stiff - it should be professional but fun

```html
<!DOCTYPE html>
<html lang="en">
<head>
<meta charset="utf-8">
<title>Pins and Dials - Agile IT Coaching and Training</title>
<link rel="stylesheet" href="https://fonts.googleapis.com/css2?family=Raleway:ital,wght@0,400;0,500;0,600;0,700;1,400;1,500&family=Libre+Baskerville:wght@400&display=swap">
<style>
:root{
  --navy:#1f2f6b;
  --ink:#233b82;
  --royal:#24408e;
  --gold:#a38e6b;
  --grey:#e8e9ef;
  --white:#ffffff;
  --footer:#1d2b5c;
  --button:#1d6fc2;
  --line:#d9d2c4;
}
*{margin:0;padding:0;box-sizing:border-box}
html,body{width:1200px;height:4468px;overflow:hidden;background:var(--white)}
body{position:relative;font-family:"Raleway",sans-serif;color:var(--ink)}
.abs{position:absolute}
/* header */
.site-header{left:0;top:0;width:1200px;height:77px;background:var(--white)}
.brand{left:156px;top:22px;display:flex;align-items:center;gap:8px;font:700 17px "Raleway",sans-serif;color:var(--royal)}
.brand-square{width:22px;height:22px;border:2px solid var(--royal)}
.nav a{position:absolute;top:33px;font:600 11px "Raleway",sans-serif;color:#1a1a1a;text-decoration:none}
.nav-cta{left:921px;top:22px;width:112px;height:35px;background:var(--button);color:var(--white);font:600 9px "Raleway",sans-serif;display:flex;align-items:center;justify-content:center;gap:8px;text-transform:uppercase}
/* hero */
.hero{left:0;top:77px;width:1200px;height:603px;background:linear-gradient(90deg,#2b3a94 0%,#3a4aa0 45%,#5b6aa8 75%,#8a90b4 100%)}
.hero-kicker{left:168px;top:190px;font:400 21px "Raleway",sans-serif;color:var(--white);display:flex;align-items:center;gap:8px}
.hero-kicker:before{content:"";width:38px;height:1px;background:var(--white);margin-top:10px}
.hero-title{left:168px;top:228px;font:400 58px/58px "Libre Baskerville",serif;color:var(--gold)}
.hero-title span{display:block;color:var(--white)}
.hero-text{left:168px;top:372px;width:400px;font:400 22px/42px "Raleway",sans-serif;color:var(--white)}
.hero-btn{left:168px;top:529px;width:113px;height:36px;background:var(--gold);color:var(--white);font:700 8px "Raleway",sans-serif;display:flex;align-items:center;justify-content:center;letter-spacing:.5px}
.social-rail{left:68px;top:317px;display:flex;flex-direction:column;gap:17px}
.social-rail i{display:block;width:14px;height:14px;background:var(--white);border-radius:3px}
/* profile */
.profile-card{left:92px;top:810px;width:1016px;height:517px;background:var(--white);border-radius:22px;box-shadow:0 10px 40px rgba(30,40,90,.12)}
.profile-photo{left:160px;top:744px;width:352px;height:517px;border-radius:20px;background:linear-gradient(160deg,#6f7a74 0%,#3b4446 55%,#1f2529 100%)}
.profile-name{left:593px;top:878px;font:600 42px "Raleway",sans-serif;color:var(--gold)}
.profile-role{left:621px;top:935px;font:italic 400 22px/36px "Raleway",sans-serif;color:var(--ink)}
.rule{height:2px;background:var(--line)}
.badges{left:593px;top:1066px;width:451px;display:flex;justify-content:space-between;padding:0 12px}
.badge{width:46px;height:46px;border-radius:50%;background:#e2a13a}
.badge.dark{background:#2c3a66;border-radius:8px;transform:rotate(45deg) scale(.8)}
.badge.sky{background:#47a6d8}
.badge.outline{background:none;border:3px solid #2c3a66;border-radius:10px}
.profile-certs{left:596px;top:1171px;width:440px;font:400 14.5px/30px "Raleway",sans-serif;color:var(--ink)}
/* experience */
.exp-title{left:0;top:1418px;width:1200px;text-align:center;font:600 40px "Raleway",sans-serif;color:var(--gold)}
.exp-sub{left:0;top:1480px;width:1200px;text-align:center;font:italic 500 22px "Raleway",sans-serif;color:var(--ink);letter-spacing:.5px}
.exp-item{top:1568px;width:300px;text-align:center}
.exp-icon{width:118px;height:118px;border-radius:50%;background:var(--royal);margin:0 auto;display:flex;align-items:center;justify-content:center}
.exp-label{margin-top:38px;font:400 22px/37px "Raleway",sans-serif;color:var(--ink)}
/* roles */
.role-photo{height:425px}
.role-kicker{font:italic 500 19px "Raleway",sans-serif;color:var(--ink)}
.role-title{font:600 42px/50px "Raleway",sans-serif;color:var(--gold)}
.role-panel{background:var(--grey)}
.role-list{list-style:none;font:400 15px/31px "Raleway",sans-serif;color:var(--ink)}
.role-list li{position:relative;padding-left:20px;margin-bottom:18px}
.role-list li:before{content:"";position:absolute;left:0;top:13px;width:7px;height:7px;border-radius:50%;background:var(--ink)}
/* footer */
.site-footer{left:0;top:4153px;width:1200px;height:315px;background:var(--footer);color:var(--white)}
.footer-brand{left:92px;top:4198px;font:400 40px "Libre Baskerville",serif;color:var(--white)}
.footer-social{top:4208px;width:30px;height:30px;border:1.5px solid var(--white);border-radius:50%}
.footer-social.solid{background:var(--white)}
.footer-rule{left:92px;top:4271px;width:1016px;height:1px;background:rgba(255,255,255,.2)}
.footer-col h4{font:600 16px "Raleway",sans-serif;margin-bottom:10px}
.footer-col p{font:400 12.5px/29px "Raleway",sans-serif;color:rgba(255,255,255,.75)}
.footer-about p{color:var(--white);font-size:12.5px}
</style>
</head>
<body>

<header class="abs site-header">
  <div class="abs brand"><span class="brand-square"></span>PINS &amp; DIALS</div>
  <nav class="nav">
    <a style="left:480px">Home</a>
    <a style="left:564px">About us</a>
    <a style="left:661px">Services</a>
    <a style="left:758px">Cases</a>
    <a style="left:841px">Blog</a>
  </nav>
  <div class="abs nav-cta">Mentor Nook
    <svg width="8" height="11" viewBox="0 0 8 11"><path d="M1 1l5 4.5L1 10" stroke="#fff" stroke-width="2" fill="none"/></svg>
  </div>
</header>

<section class="abs hero" role="img" aria-label="Two professionals shaking hands in an office, under a blue overlay"></section>
<div class="abs social-rail"><i></i><i></i><i></i><i></i></div>
<div class="abs hero-kicker">Agile IT Coaching and Training</div>
<h1 class="abs hero-title">Pins and Dials<span>company</span></h1>
<p class="abs hero-text">Demonstrate experience and progression from Scrum Master to Program Manager to Coach</p>
<div class="abs hero-btn">LEARN MORE</div>

<section class="abs profile-card"></section>
<div class="abs profile-photo" role="img" aria-label="Portrait of the coach in a suit talking on a phone"></div>
<h2 class="abs profile-name">Brent Holloway</h2>
<p class="abs profile-role">Senior Scrum Master &amp;<br>Team Agile Coach</p>
<div class="abs rule" style="left:593px;top:1033px;width:451px"></div>
<div class="abs badges">
  <span class="badge outline"></span><span class="badge"></span><span class="badge sky"></span><span class="badge dark"></span><span class="badge" style="background:#edb62d"></span>
</div>
<div class="abs rule" style="left:593px;top:1144px;width:451px"></div>
<p class="abs profile-certs">PSC-SP, Certified Sprint Foundations Educator, TAC-AC,<br>LYNQ Advanced Scrum Master, A-PSC</p>

<h2 class="abs exp-title">What Is My Experience?</h2>
<p class="abs exp-sub">As a Senior Scrum Master &amp; Team Agile Coach</p>

<div class="abs exp-item" style="left:42px">
  <div class="exp-icon"><svg width="70" height="70" viewBox="0 0 70 70" fill="none" stroke="#fff" stroke-width="2"><circle cx="35" cy="35" r="33"/><circle cx="35" cy="22" r="8"/><path d="M22 50c0-10 6-15 13-15s13 5 13 15z"/><path d="M30 56h10M31 60h8"/></svg></div>
  <p class="exp-label">As a LYNQ Adv<br>Scrum Master</p>
</div>
<div class="abs exp-item" style="left:450px">
  <div class="exp-icon"><svg width="70" height="70" viewBox="0 0 70 70" fill="none" stroke="#fff" stroke-width="2"><circle cx="35" cy="35" r="33"/><circle cx="35" cy="28" r="6"/><circle cx="21" cy="30" r="5"/><circle cx="49" cy="30" r="5"/><path d="M25 46c0-7 4-11 10-11s10 4 10 11M12 44c0-6 4-9 9-9M58 44c0-6-4-9-9-9"/></svg></div>
  <p class="exp-label">As a Hybrid Scrum<br>Master Project<br>Manager</p>
</div>
<div class="abs exp-item" style="left:835px">
  <div class="exp-icon"><svg width="70" height="70" viewBox="0 0 70 70" fill="none" stroke="#fff" stroke-width="2"><circle cx="35" cy="35" r="33"/><path d="M26 56V46c-5-3-8-8-8-14 0-9 8-16 17-16s17 7 17 16l3 8-4 1v6h-7v9"/><circle cx="36" cy="31" r="6"/><circle cx="36" cy="31" r="2"/></svg></div>
  <p class="exp-label">As a Business<br>Transformation Program<br>Manager</p>
</div>

<!-- Role 1 -->
<div class="abs role-photo" style="left:92px;top:1958px;width:501px;background:linear-gradient(120deg,#d8d4cc,#9a918a 55%,#5f5650)" role="img" aria-label="Team meeting around a table with tablets"></div>
<p class="abs role-kicker" style="left:648px;top:1988px">As A</p>
<h3 class="abs role-title" style="left:648px;top:2016px">LYNQ Adv Scrum<br>Master</h3>
<div class="abs role-panel" style="left:593px;top:2133px;width:519px;height:517px"></div>
<ul class="abs role-list" style="left:676px;top:2167px;width:360px">
  <li>Stand up teams</li>
  <li>Run development efforts concurrently leading multiple teams</li>
  <li>Run LYNQ ceremonies</li>
  <li>Scrum of Scrums facilitator</li>
  <li>PI Planning team facilitator (multiple teams on BQR)</li>
  <li>Teach and coach to advanced development team strategies</li>
  <li>Lead program level communications and business status updates on behalf of the team</li>
</ul>

<!-- Role 2 -->
<p class="abs role-kicker" style="left:147px;top:2734px">As A</p>
<h3 class="abs role-title" style="left:147px;top:2762px">Hybrid Scrum Master<br>Project Manager</h3>
<div class="abs role-panel" style="left:92px;top:2885px;width:520px;height:420px"></div>
<ul class="abs role-list" style="left:173px;top:2918px;width:340px">
  <li>Stand up teams</li>
  <li>run multiple program level projects simultaneously</li>
  <li>implement custom hybrid development strategies</li>
  <li>manage to project triple constraints</li>
  <li>communications lead and business liaison</li>
  <li>use multiple coaching styles based on team and project</li>
</ul>
<div class="abs role-photo" style="left:612px;top:2714px;width:498px;background:linear-gradient(150deg,#c9ccd0,#8c97a6 50%,#4f5a68)" role="img" aria-label="Overhead view of three colleagues working at laptops"></div>

<!-- Role 3 -->
<div class="abs role-photo" style="left:92px;top:3369px;width:498px;background:linear-gradient(110deg,#e4e6ea,#9ba3ad 50%,#3e4a5a)" role="img" aria-label="Hands typing on a laptop keyboard"></div>
<p class="abs role-kicker" style="left:648px;top:3403px">As A</p>
<h3 class="abs role-title" style="left:646px;top:3433px;line-height:46px">Business Transformation<br>Program Manager</h3>
<div class="abs role-panel" style="left:590px;top:3548px;width:518px;height:511px"></div>
<ul class="abs role-list" style="left:672px;top:3580px;width:350px">
  <li>lead business transformation efforts at the program level</li>
  <li>work with multiple product owners, business analysts, and business stakeholders on requirements</li>
  <li>lead the international rollout, onboarding, and support of new transformational CRM tool, Cloudora</li>
  <li>lead the international rollout, onboarding, and support of new transformational CRM tool, Cloudora</li>
  <li>Serve as program organization and communications lead</li>
</ul>

<footer class="abs site-footer"></footer>
<div class="abs footer-brand">Brent Holloway</div>
<span class="abs footer-social" style="left:946px"></span>
<span class="abs footer-social" style="left:989px"></span>
<span class="abs footer-social" style="left:1032px"></span>
<span class="abs footer-social solid" style="left:1077px"></span>
<div class="abs footer-rule"></div>
<div class="abs footer-col footer-about" style="left:92px;top:4310px;width:320px">
  <h4>Agile IT Coaching and Training</h4>
  <p>Demonstrate experience and progression<br>from Scrum Master to Program Manager to Coach</p>
</div>
<div class="abs footer-col" style="left:534px;top:4310px"><h4>About me</h4><p>Coaching Designations<br>My experience<br>Roles</p></div>
<div class="abs footer-col" style="left:730px;top:4310px"><h4>Coaching</h4><p>Multiple Teams<br>Multiple Players<br>Business</p></div>
<div class="abs footer-col" style="left:884px;top:4310px"><h4>Team Level</h4><p>Scrum Values<br>principles<br>Coaching &amp; Running</p></div>

</body>
</html>
```